Starvu Review Divorce Law Firm Folder Insert

We are a divorce law firm.

We need a flyer just like the one that is posted. For example, that allows for our Starvu reviews to be a good deed. We do like the coloring we will provide the image that goes on the bottom right. We are open to any design. Any thoughts people have, and unique designs are welcome were very happy with this example. However, we want people to know to have some background as to what would be the best option.

Again anything but again we do want the Starvu has to be the five stars in my logo has to be on there and the portion that says these different comments included

Target Market(s)

Divorce and Custody Clients

Industry/Entity Type

Legal

Requirements
Must have
• what must remain is the Starvu logo that large, and the five stars in the front in the back. What must be included is the Starvu reviews listed below. Not all of them must be used but no less than five must be used. At least one of the five

1.) “Worth the money!”
2.) “Simply the best”
3.) “So much knowledge and experience”
4.) “When life gets challenging, you want Marcus on your team!”
5.) “He made a painful divorce and custody, much easier to deal with”
6.) “Willingness to go the extra mile”
7.) “Respectful and caring”
8.) “I wouldn’t go with anyone else!”
Nice to have
• We are a divorce law firm in Harrisburg Pennsylvania. we need a Starvu review insert for our potential new clients folder. We need a hard insert flyer around 6 x 9 in height as similar possible to the one included as an attached, however we are open to any design. Since like the example so much the is a great guidepost.

We appreciate unique designs but have found one we have. To be very much to our liking. We are open to any other signs, but again. One example. Any thoughts people have, and unique designs are welcome were very happy with this example. However, we want people to know to have some background as to what would be the best option.

Attached you will find our logo, our shield by itself, the example card, and three images from which you should pick one.

one possibly to the photos can be included, but not aall three, included are three photos, only one should be used. Please pick one and use it
Should not have
• Look far off of a look that I too crazy

```html
<!DOCTYPE html>
<html lang="en">
<head>
<meta charset="utf-8">
<title>Marcus R Holloway – Starvu Review Inserts</title>
<link href="https://fonts.googleapis.com/css2?family=Cinzel:wght@400;600;700;800&display=swap" rel="stylesheet">
<style>
  :root {
    --stage: #303030;
    --navy: #0c1a4a;
    --navy-deep: #081238;
    --yellow: #e6e04a;
    --yellow-soft: #efe98a;
    --gold-star: #f5b50a;
    --ink: #141414;
    --paper: #ffffff;
    --mist: #e6e8ec;
    --grey-text: #6b6e78;
  }
  * { margin: 0; padding: 0; box-sizing: border-box; }
  html, body { width: 1200px; height: 900px; overflow: hidden; }
  body { background: var(--stage); font-family: "Cinzel", serif; position: relative; }

  .flyer { position: absolute; background: var(--paper); overflow: hidden; }
  .flyer--front { left: 70px; top: 94px; width: 486px; height: 688px; }
  .flyer--back { left: 616px; top: 98px; width: 483px; height: 682px; }
  .abs { position: absolute; }
  .centered { left: 0; right: 0; text-align: center; }

  /* ---------- front ---------- */
  .front-header { left: 0; top: 0; width: 486px; height: 121px;
    background: linear-gradient(90deg, var(--navy-deep), #1c2d66 55%, var(--navy)); }
  .tagline-small { left: 26px; top: 28px; color: var(--paper); font-size: 12.5px; font-weight: 600; letter-spacing: .3px; }
  .tagline-large { left: 31px; top: 48px; color: var(--paper); font-size: 21px; font-weight: 700; }
  .firm-mark { left: 254px; top: 38px; display: flex; align-items: center; gap: 8px; color: var(--paper); font-weight: 400; }
  .firm-mark__square { width: 30px; height: 30px; border: 2px solid var(--paper); }
  .firm-mark__name { font-size: 15px; line-height: 1.05; }
  .firm-mark__name small { display: block; font-size: 8px; letter-spacing: .4px; }

  .bar-navy-top { left: 0; top: 134px; width: 210px; height: 16px; background: var(--navy); }
  .bar-yellow-top { left: 210px; top: 131px; width: 276px; height: 22px; background: var(--yellow); }
  .hero { left: 0; top: 153px; width: 486px; height: 215px;
    background: linear-gradient(90deg, #dcdfe4, #eef0f2 60%, #d8dadf); }
  .hero-portrait { left: 0; top: 153px; width: 195px; height: 215px;
    background: linear-gradient(180deg, #6f6a66, #262c3d 55%, #1b2034); }
  .hero-title { left: 195px; top: 214px; width: 291px; text-align: center; color: var(--navy); }
  .hero-title .big { font-size: 38px; font-weight: 800; line-height: 1; }
  .hero-title .sub { font-size: 17.5px; font-weight: 700; line-height: 1.22; color: var(--ink); }
  .hero-url { left: 195px; top: 308px; width: 291px; text-align: center; font-size: 10px; letter-spacing: 2px; color: var(--grey-text); }
  .bar-yellow-bottom { left: 0; top: 361px; width: 320px; height: 22px; background: var(--yellow); }
  .bar-navy-bottom { left: 320px; top: 368px; width: 166px; height: 8px; background: var(--navy); }

  .brand-word { font-weight: 700; color: var(--navy); letter-spacing: 1px; }
  .front-brand { top: 402px; font-size: 44px; }
  .stars { color: var(--gold-star); letter-spacing: 2px; }
  .front-stars { top: 442px; font-size: 44px; }
  .review-band { background: linear-gradient(90deg, transparent, var(--mist) 20%, var(--mist) 80%, transparent); }
  .front-band { left: 20px; top: 502px; width: 446px; height: 30px; }
  .front-band span, .back-band span { display: block; text-align: center; font-weight: 700; color: var(--ink); }
  .front-band span { font-size: 20px; line-height: 30px; }
  .skyline { left: 0; top: 535px; width: 486px; height: 117px;
    background: linear-gradient(180deg, #ffffff, #e3e5e9 60%, #cfd2d8); }
  .consult { top: 556px; font-size: 17px; font-weight: 700; color: var(--ink); }
  .phone { top: 574px; font-size: 52px; font-weight: 400; color: var(--navy); letter-spacing: 1px; }
  .footer { background: var(--navy); color: var(--paper); font-size: 9.5px; letter-spacing: .5px; display: flex; align-items: center; }
  .front-footer { left: 0; top: 652px; width: 486px; height: 24px; justify-content: center; }
  .front-foot-fade { left: 0; top: 676px; width: 486px; height: 12px; background: linear-gradient(180deg, #d7d9de, #f5f5f7); }

  /* ---------- back ---------- */
  .back-bar-yellow { left: 0; top: 17px; width: 483px; height: 17px; background: var(--yellow); }
  .back-banner { left: 0; top: 45px; width: 483px; height: 197px;
    background: linear-gradient(90deg, var(--navy-deep), var(--navy) 45%, #3b4a72 75%, #5d6784); }
  .statue { left: 310px; top: 45px; width: 160px; height: 197px;
    background: linear-gradient(180deg, #8a6a45, #5b3f23 70%, #3b2a1a); opacity: .85; }
  .banner-copy { left: 0; top: 86px; width: 310px; text-align: center; line-height: 1.05; }
  .banner-copy .white { color: var(--paper); font-weight: 400; }
  .banner-copy .gold { color: var(--yellow); font-weight: 700; }
  .banner-copy .l1 { font-size: 32px; }
  .banner-copy .l2 { font-size: 28px; }
  .banner-copy .l3 { font-size: 24px; }
  .banner-copy .l4 { font-size: 17.5px; }
  .back-mark { left: 60px; top: 280px; display: flex; align-items: center; gap: 6px; color: var(--navy); font-size: 15px; font-weight: 700; line-height: 1.1; }
  .back-mark__square { width: 22px; height: 22px; background: var(--navy); }
  .back-brand { left: 170px; top: 253px; width: 240px; text-align: center; font-size: 52px; }
  .back-stars { left: 160px; top: 302px; width: 260px; text-align: center; font-size: 44px; }
  .back-band { left: 0; top: 369px; width: 483px; height: 26px;
    background: linear-gradient(90deg, transparent, var(--yellow-soft) 15%, #f7f4c8 70%, transparent); }
  .back-band span { font-size: 17px; line-height: 26px; }
  .reviews-bg { left: 0; top: 400px; width: 483px; height: 247px;
    background: linear-gradient(180deg, #ffffff, #eef0f3); }
  .review { position: absolute; font-size: 10.5px; font-weight: 700; color: var(--ink); line-height: 1.25; }
  .review .stars { font-size: 11px; letter-spacing: 0; margin-right: 4px; }
  .back-footer { left: 0; top: 647px; width: 483px; height: 24px; }
  .back-footer span { flex: 1; text-align: center; }
  .back-footer span + span { border-left: 1px solid #4a5890; }
</style>
</head>
<body>

<section class="flyer flyer--front" aria-label="Front of review insert">
  <div class="abs front-header" role="img" aria-label="Dark navy photograph of courthouse columns"></div>
  <p class="abs tagline-small">MAKING A DIFFERENCE IN OUR</p>
  <p class="abs tagline-large">CLIENTS' LIVES</p>
  <div class="abs firm-mark">
    <span class="firm-mark__square"></span>
    <span class="firm-mark__name"><small>THE LAW OFFICE OF</small>MARCUS R HOLLOWAY</span>
  </div>

  <div class="abs bar-navy-top"></div>
  <div class="abs bar-yellow-top"></div>
  <div class="abs hero" role="img" aria-label="Faded photograph of a client reviewing documents"></div>
  <div class="abs hero-portrait" role="img" aria-label="Portrait of the attorney in a dark suit leaning on a railing"></div>
  <div class="abs hero-title">
    <p class="big">PROVIDING</p>
    <p class="sub">OUR CLIENTS WITH THE<br>SERVICE THEY DESERVE</p>
  </div>
  <p class="abs hero-url">WWW.MARCUSHOLLOWAYLAW.COM</p>
  <div class="abs bar-yellow-bottom"></div>
  <div class="abs bar-navy-bottom"></div>

  <p class="abs centered brand-word front-brand">Starvu</p>
  <p class="abs centered stars front-stars">★★★★★</p>
  <div class="abs skyline" role="img" aria-label="Faint photograph of the Harrisburg skyline"></div>
  <div class="abs review-band front-band"><span>Check out our review on Starvu</span></div>
  <p class="abs centered consult">COMPLIMENTARY CONSULTATIONS</p>
  <p class="abs centered phone">717.555.0143</p>
  <div class="abs footer front-footer">2150 Ridgeview Road Suite 210, Harrisburg, PA 17110</div>
  <div class="abs front-foot-fade"></div>
</section>

<section class="flyer flyer--back" aria-label="Back of review insert">
  <div class="abs back-bar-yellow"></div>
  <div class="abs back-banner" role="img" aria-label="Blurred photograph of courthouse columns in navy tones"></div>
  <div class="abs statue" role="img" aria-label="Bronze statue of Lady Justice holding scales"></div>
  <div class="abs banner-copy">
    <p class="white l1">OFFERING</p>
    <p class="gold l2">COMPREHENSIVE</p>
    <p class="white l3">LEGAL ADVICE FOR</p>
    <p class="gold l4">CENTRAL PENNSYLVANIA</p>
  </div>

  <div class="abs back-mark"><span class="back-mark__square"></span><span>HOLLOWAY<br>LAW</span></div>
  <p class="abs brand-word back-brand">Starvu</p>
  <p class="abs stars back-stars">★★★★★</p>
  <div class="abs back-band"><span>Check out our review on Starvu</span></div>

  <div class="abs reviews-bg" role="img" aria-label="Faint photograph of white columns"></div>
  <p class="review" style="left:21px;top:424px;"><span class="stars">★★★★★</span>I WOULDN'T GO WITH<br>ANYONE ELSE!</p>
  <p class="review" style="left:21px;top:466px;"><span class="stars">★★★★★</span>SO MUCH KNOWLEDGE AND<br>EXPERIENCE</p>
  <p class="review" style="left:21px;top:516px;"><span class="stars">★★★★★</span>WHEN LIFE GETS CHALLENGING,<br>YOU WANT MARCUS ON YOUR TEAM!</p>
  <p class="review" style="left:21px;top:567px;"><span class="stars">★★★★★</span>HE MADE A PAINFUL DIVORCE<br>AND CUSTODY, MUCH EASIER TO DEAL<br>WITH</p>
  <p class="review" style="left:294px;top:423px;"><span class="stars">★★★★★</span>WORTH THE<br>MONEY!</p>
  <p class="review" style="left:294px;top:467px;"><span class="stars">★★★★★</span>SIMPLY THE BEST</p>
  <p class="review" style="left:294px;top:517px;"><span class="stars">★★★★★</span> RESPECTFUL</p>
  <p class="review" style="left:294px;top:567px;"><span class="stars">★★★★★</span>WILLINGNESS TO<br>GO THE EXTRA MILE</p>

  <div class="abs footer back-footer">
    <span>WWW.MARCUSHOLLOWAYLAW.COM</span>
    <span>2150 Ridgeview Road Suite 210, Harrisburg, PA 17110</span>
  </div>
</section>

</body>
</html>
```